We would like a new design for our company Christmas Card. The design must have an orange background and have a festive theme.

The size of the card should be DL (210mm x 99mm).

Message on front cover: Merry Christmas
Message inside: Our warmest wishes for a wonderful Christmas and a very Happy New Year
From the team at under painted skies and kettle-spark

Please see attached example of the card that we used last year.

Industry/Entity Type

It Company

Colors
f78f20

Requirements
Must have
• Orange as the main colour
• A new design
• Font - Helevetica Neue Light (not condensed)

```html
<!DOCTYPE html>
<html lang="en">
<head>
<meta charset="utf-8">
<title>Christmas Card – under painted skies and kettle-spark</title>
<link rel="stylesheet" href="https://fonts.googleapis.com/css2?family=Great+Vibes&family=Roboto:wght@300&display=swap">
<style>
  :root {
    --orange: #f78f20;
    --orange-soft: #f9a64c;
    --paper: #ffffff;
    --stage: #1c1c1c;
    --cream: #fff6ec;
  }
  * { box-sizing: border-box; margin: 0; padding: 0; }
  html, body {
    width: 1200px;
    height: 694px;
    overflow: hidden;
    background: var(--stage);
  }
  .canvas {
    position: relative;
    width: 1200px;
    height: 694px;
  }
  .front-cover {
    position: absolute;
    left: 38px;
    top: 170px;
    width: 540px;
    height: 255px;
    background: var(--orange);
    overflow: hidden;
  }
  .front-cover__greeting {
    position: absolute;
    left: 58px;
    top: 100px;
    font-family: "Great Vibes", cursive;
    font-size: 50px;
    font-weight: 400;
    color: var(--cream);
    letter-spacing: 0.5px;
  }
  .ornaments {
    position: absolute;
    inset: 0;
    width: 100%;
    height: 100%;
  }
  .inside-panel {
    position: absolute;
    left: 621px;
    top: 91px;
    width: 546px;
    height: 513px;
    background: var(--paper);
    overflow: hidden;
  }
  .inside-panel__message {
    position: absolute;
    left: 67px;
    top: 365px;
    font-family: "Roboto", "Helvetica Neue", sans-serif;
    font-weight: 300;
    font-size: 16.5px;
    line-height: 21px;
    color: var(--orange);
  }
  .inside-panel__signoff {
    position: absolute;
    left: 67px;
    top: 441px;
    font-family: "Roboto", "Helvetica Neue", sans-serif;
    font-weight: 300;
    font-size: 9.5px;
    color: var(--orange);
  }
</style>
</head>
<body>
<main class="canvas">

  <section class="front-cover">
    <svg class="ornaments" viewBox="0 0 540 255" role="img" aria-label="White swirled snowflake ornaments on the right of the cover">
      <defs>
        <radialGradient id="flake-light" cx="50%" cy="50%" r="50%">
          <stop offset="0%" stop-color="#ffffff" stop-opacity="0.75"/>
          <stop offset="100%" stop-color="#ffffff" stop-opacity="0.15"/>
        </radialGradient>
      </defs>
      <circle cx="430" cy="120" r="92" fill="url(#flake-light)"/>
      <circle cx="520" cy="20" r="48" fill="url(#flake-light)"/>
      <circle cx="525" cy="210" r="32" fill="url(#flake-light)"/>
    </svg>
    <h1 class="front-cover__greeting">Merry Christmas</h1>
  </section>

  <section class="inside-panel">
    <svg class="ornaments" viewBox="0 0 546 513" role="img" aria-label="Orange swirled snowflake ornaments falling down the right side">
      <defs>
        <radialGradient id="flake-orange" cx="50%" cy="50%" r="50%">
          <stop offset="0%" stop-color="#f78f20" stop-opacity="0.85"/>
          <stop offset="100%" stop-color="#f78f20" stop-opacity="0.2"/>
        </radialGradient>
      </defs>
      <circle cx="446" cy="61" r="16" fill="url(#flake-orange)"/>
      <circle cx="487" cy="98" r="18" fill="url(#flake-orange)"/>
      <circle cx="441" cy="155" r="30" fill="url(#flake-orange)"/>
      <circle cx="512" cy="250" r="75" fill="url(#flake-orange)"/>
      <circle cx="424" cy="380" r="95" fill="url(#flake-orange)"/>
      <circle cx="517" cy="480" r="36" fill="url(#flake-orange)"/>
    </svg>
    <p class="inside-panel__message">
      Our warmest wishes<br>
      for a wonderful Christmas<br>
      and a very Happy New Year
    </p>
    <p class="inside-panel__signoff">From the team at under painted skies and kettle-spark</p>
  </section>

</main>
</body>
</html>
```